Premium Juice and Wine Bottle Label

We require a premium label design for a Burgundy style wine bottle - the design should reflect pure and organic theme, with a reference to New Zealand blueberries. The winning design will look high-end, simple but sophisticated. Our logo is attached, refer :

https://www.orvalecellars.co.nz and https://www.pirovane.co.nz/wines/details/coming-soon-showcase/2018

for inspiration.

Target Market(s)

High-end retail grocery stores, wine shops, bars.

Requirements
Must have
• Label should leave enough space for barcode and nutrients/ingredients etc. Reference to New Zealand, natural-beverage, be very high-end in design. Refer links in project description for inspiration. Refer to attached logo, which must be used - feel free to change colour in order to obtain the best high-class design.
Nice to have
• N/A.
Should not have
• Cartoons or pictures of berries.

```html
<!DOCTYPE html>
<html lang="en">
<head>
<meta charset="utf-8">
<title>Harlow Lane — Organic Label</title>
<link rel="stylesheet" href="https://fonts.googleapis.com/css2?family=Bodoni+Moda:wght@400&display=swap">
<style>
  :root {
    --backdrop: #efefef;
    --paper: #f8f3ea;
    --wine: #8a0020;
    --sprig: #ece4d8;
  }
  html, body {
    margin: 0;
    padding: 0;
    width: 1200px;
    height: 1200px;
    overflow: hidden;
    background: var(--backdrop);
  }
  .canvas {
    position: relative;
    width: 1200px;
    height: 1200px;
  }
  .label {
    position: absolute;
    left: 210px;
    top: 110px;
    width: 780px;
    height: 980px;
    background: var(--paper);
    box-shadow: 0 2px 10px rgba(0,0,0,0.08);
    font-family: "Bodoni Moda", "Didot", serif;
    color: var(--wine);
  }
  .label-frame {
    position: absolute;
    left: 50px;
    top: 55px;
    right: 48px;
    bottom: 36px;
    border: 2px solid var(--wine);
  }
  .berry-field {
    position: absolute;
    left: 0;
    right: 0;
    bottom: 0;
    height: 190px;
    background: linear-gradient(to bottom, rgba(236,228,216,0) 0%, var(--sprig) 100%);
  }
  .brand {
    position: absolute;
    left: 0;
    right: 0;
    top: 190px;
    text-align: center;
  }
  .brand-mark {
    display: block;
    width: 14px;
    height: 14px;
    margin: 0 auto 18px;
    background: var(--wine);
  }
  .brand-name {
    font-size: 74px;
    line-height: 1;
    font-weight: 400;
    margin: 0;
  }
  .variety {
    position: absolute;
    left: 0;
    right: 0;
    top: 465px;
    text-align: center;
  }
  .variety-title {
    font-size: 66px;
    line-height: 1;
    letter-spacing: 1px;
    margin: 0;
    font-weight: 400;
  }
  .variety-sub {
    font-size: 38px;
    line-height: 1;
    letter-spacing: 1px;
    margin: 14px 0 0;
    font-weight: 400;
  }
  .origin {
    position: absolute;
    left: 0;
    right: 0;
    top: 800px;
    text-align: center;
    font-size: 28px;
    letter-spacing: 4px;
    margin: 0;
    font-weight: 400;
  }
</style>
</head>
<body>
  <div class="canvas">
    <section class="label">
      <div class="berry-field" role="img" aria-label="Faint line-drawn blueberry sprigs across the foot of the label"></div>
      <div class="label-frame"></div>
      <header class="brand">
        <span class="brand-mark"></span>
        <h1 class="brand-name">Harlow Lane</h1>
      </header>
      <div class="variety">
        <h2 class="variety-title">ORGANIC</h2>
        <p class="variety-sub">WINE BOTTLES</p>
      </div>
      <p class="origin">NEW ZEALAND BLUEBERRIRS</p>
    </section>
  </div>
</body>
</html>
```